Economics and Investing for women with a humorous narrative

I need a logo and business card design for my company:
The Velvet Sparrow LLC. TVS is an educational website dedicated to translating the language of economics and investing into concepts that are interesting, easy to understand and funny.
As the target market is for women, the card needs to be NON traditional in terms of finance and investing. No pictures of charts, currencies, stock markets etc. This needs to be colorful , inviting and memorable.
The driver of the site is to present difficult concepts with a humorous tilt. If Dorian Hale (The Paper Orchard) collaborated with Jolene Pratt what would it look like?

Reason: I don't think I did a good enough job of explaining what I was looking for including the type of color palette. I asked that the cards NOT look so corporate. I have updated my brief and included 3 pictures of a color scheme I like along with design. I also update the information to be included on the card.

Target Market(s)

Women 30-50

Industry/Entity Type

Business

Contact Information for Business Card

The Velvet Sparrow LLC
Wanda Klose , CEO
382 Garnet Street
Suite 2700
New York, New York 10122

Phone: 212-555-0143
TheVelvetSparrow.com
Email: wanda@thevelvetsparrow.com

Font styles to use
Other font styles liked:
• LustPro Demi No.3

Requirements
Must have
• Gravitas, bold warm colors, the antithesis of modest
Nice to have
• Isn't this why I am hiring designers?
Should not have
• Charts, graphs, numbers, currency, stock or bond market pictures, any reference to investing . Do not want this to look like a boring investment business card

```html
<!DOCTYPE html>
<html lang="en">
<head>
<meta charset="utf-8">
<title>The Velvet Sparrow LLC – Business Card</title>
<link rel="stylesheet" href="https://fonts.googleapis.com/css2?family=Source+Sans+3:wght@400;600;700&display=swap">
<style>
  :root {
    --velvet: #8c1d47;
    --velvet-deep: #6e1438;
    --coral: #e8643c;
    --gold: #f0a830;
    --ink: #2b2124;
    --paper: #fffaf5;
    --backdrop: #ece6e1;
    --icon: #ffffff;
  }
  * { margin: 0; padding: 0; box-sizing: border-box; }
  html, body {
    width: 1200px; height: 900px; overflow: hidden;
    background: var(--backdrop);
    font-family: "Source Sans 3", "Myriad Pro", Arial, sans-serif;
  }
  .canvas { position: relative; width: 1200px; height: 900px; }

  .card {
    position: absolute;
    background: var(--paper);
    box-shadow: 0 6px 18px rgba(0,0,0,.18);
  }

  /* Front */
  .card-front { left: 78px; top: 35px; width: 587px; height: 362px; }
  .side-band {
    position: absolute; left: 29px; width: 126px;
    background: linear-gradient(180deg, var(--velvet) 0%, var(--velvet-deep) 100%);
  }
  .side-band--top { top: 0; height: 58px; }
  .side-band--bottom { top: 148px; bottom: 0; }

  .front-mark {
    position: absolute; left: 30px; top: 72px;
    font-weight: 700; font-size: 56px; line-height: 1;
    color: var(--coral); letter-spacing: -1px;
  }
  .front-company {
    position: absolute; left: 174px; top: 88px;
    font-weight: 600; font-size: 22px; color: var(--velvet);
    white-space: nowrap;
  }
  .llc { font-size: 12px; margin-left: 4px; }

  .holder {
    position: absolute; left: 174px; top: 166px;
    font-weight: 600; font-size: 22px; color: var(--velvet);
  }
  .holder .title { font-size: 16px; }

  .rule {
    position: absolute; left: 174px; width: 191px; height: 2px; background: var(--gold);
  }
  .rule--one { top: 201px; }
  .rule--two { top: 259px; }

  .address, .contacts {
    position: absolute; left: 174px;
    font-size: 16px; line-height: 22px; color: var(--ink);
  }
  .address { top: 210px; }
  .contacts { top: 270px; line-height: 24.5px; }

  .contact-icons {
    position: absolute; left: 129px; top: 276px;
    display: flex; flex-direction: column; gap: 12.5px;
  }
  .contact-icons svg { width: 12px; height: 12px; display: block; }

  /* Back */
  .card-back {
    left: 388px; top: 505px; width: 567px; height: 352px;
    background: linear-gradient(135deg, var(--velvet) 0%, var(--velvet-deep) 100%);
  }
  .back-mark {
    position: absolute; left: 0; right: 0; top: 104px; text-align: center;
    font-weight: 700; font-size: 96px; line-height: 1;
    color: var(--gold); letter-spacing: -2px;
  }
  .back-company {
    position: absolute; left: 0; right: 0; top: 218px; text-align: center;
    font-weight: 600; font-size: 25px; color: var(--paper); white-space: nowrap;
  }
</style>
</head>
<body>
<div class="canvas">

  <section class="card card-front" aria-label="Business card front">
    <div class="side-band side-band--top"></div>
    <div class="side-band side-band--bottom"></div>

    <div class="front-mark">TVS</div>
    <div class="front-company">THE VELVET SPARROW<span class="llc">LLC</span></div>

    <div class="holder">Wanda Klose <span class="title">, CEO</span></div>
    <div class="rule rule--one"></div>
    <div class="address">382 Garnet Street Suite 2700<br>New York, New York 10122</div>
    <div class="rule rule--two"></div>

    <div class="contact-icons" aria-hidden="true">
      <svg viewBox="0 0 12 12"><path fill="var(--icon)" d="M2.3 0.8l2 2-1 1.4c.7 1.6 2 2.9 3.6 3.6l1.4-1 2 2-1.2 1.6C5.6 10.2 1.8 6.4 0.6 2z"/></svg>
      <svg viewBox="0 0 12 12"><rect x="0.8" y="2.3" width="10.4" height="7.4" fill="none" stroke="var(--icon)" stroke-width="1"/><path d="M0.8 2.6L6 6.6l5.2-4" fill="none" stroke="var(--icon)" stroke-width="1"/></svg>
      <svg viewBox="0 0 12 12"><g fill="none" stroke="var(--icon)" stroke-width="0.9"><circle cx="6" cy="6" r="5"/><ellipse cx="6" cy="6" rx="2.2" ry="5"/><path d="M1 6h10M1.8 3.4h8.4M1.8 8.6h8.4"/></g></svg>
    </div>

    <div class="contacts">
      212-555-0143<br>
      wanda@thevelvetsparrow.com<br>
      www.TheVelvetSparrow.com
    </div>
  </section>

  <section class="card card-back" aria-label="Business card back">
    <div class="back-mark">TVS</div>
    <div class="back-company">THE VELVET SPARROW<span class="llc">LLC</span></div>
  </section>

</div>
</body>
</html>
```